GUARANTEED! Simple website for independent event planner and consultant...

I need a website that is no more than 5 or 6 pages to illustrate who I am and what I can offer to groups who book hotels for meetings and conferences. I have 20 years of experience planning meetings within hotels and I am now ready to go out on my own and help clients choose venues, negotiate contracts and plan effective meetings. I will focus on clients planning meetings in the mountains of Colorado but I am willing to travel as well. I want to work with a person who is collaborative and can direct me on what they need to move the project along quickly. I already have my logo, a hosting site and work e-mail address. Also, I recently hired a photographer to do head shots. Lastly, it important for me to be able to talk on the phone or skype with this person, as needed and I must be able to make changes to my site down the road when necessary...

Target Market(s)

Corporate Groups

Industry/Entity Type

Event Planning

Coding

Coded - Design and coding required

Number of Pages Required

5+ page

Font styles to use
Sans Serif

Requirements
Must have
• About me page, event planning services offered page, task force and consulting work page, testimonials page, page for blogs, page to contact me/request a proposal. May need advice on what else I need...
Nice to have
• I want it to look sharp and professional. I want people to look at my site and know immediately that they can trust me and the work I can do.
• I don't want it to look like it is over the top as I am not a HUGE company but I do want it to be professional and easy to view and navigate.
Should not have
• Bright colors
• My logo is bright orange and black. I have also used dark grey and orange. See below:
• Orange:
• C = 0
• M = 64
• Y = 100
• K = 0
• Gray:
• C = 67
• M = 60
• Y = 59
• K = 45
• Font: Gotham Book and Gotham Bold

```html
<!DOCTYPE html>
<html lang="en">
<head>
<meta charset="UTF-8">
<title>Testimonials</title>
<link href="https://fonts.googleapis.com/css2?family=Poppins:wght@600;700&family=Lato:wght@400&display=swap" rel="stylesheet">
<style>
  :root {
    --orange: #f47b20;
    --ink: #555555;
    --muted: #8a8a8a;
    --quote: #999999;
    --white: #ffffff;
    --paper: #f6f6f6;
    --hatch: #efefef;
  }
  * { margin: 0; padding: 0; box-sizing: border-box; }
  html, body { width: 1200px; height: 546px; overflow: hidden; background: var(--white); }
  .page { position: relative; width: 1200px; height: 546px; overflow: hidden; font-family: "Lato", sans-serif; }

  .top-band {
    position: absolute; left: 0; top: 0; width: 1200px; height: 53px;
    background: repeating-linear-gradient(135deg, var(--paper) 0 3px, var(--hatch) 3px 4px);
  }

  .testimonials {
    position: absolute; left: 0; top: 53px; width: 1200px; height: 402px;
  }
  .testimonials-backdrop {
    position: absolute; inset: 0;
    background:
      linear-gradient(180deg, rgba(255,255,255,0) 0%, rgba(255,255,255,0) 40%, rgba(0,0,0,0.55) 75%, rgba(0,0,0,0.7) 100%),
      linear-gradient(90deg, #000 0%, #0a0a0a 11%, #3a3a3a 18%, #d8d8d8 28%, #ececec 50%, #d9d9d9 70%, #6a6a6a 78%, #0b0b0b 84%, #000 100%);
  }
  .section-title {
    position: absolute; left: 0; width: 1200px; top: 80px;
    text-align: center; font-family: "Poppins", sans-serif; font-weight: 700;
    font-size: 24px; line-height: 1; color: var(--orange);
  }
  .testimonials .section-title { top: 27px; }
  .avatar {
    position: absolute; left: 560px; top: 84px; width: 80px; height: 80px;
    border-radius: 50%;
    background: radial-gradient(circle at 60% 45%, #5c5c5c 0%, #3a3a3a 60%, #2a2a2a 100%);
  }
  .quote-card {
    position: absolute; left: 292px; top: 190px; width: 616px; height: 113px;
    background: var(--white);
    display: flex; align-items: center; justify-content: center;
    padding: 0 26px;
  }
  .quote-card p {
    text-align: center; font-size: 9.6px; line-height: 16.4px; color: var(--quote);
  }
  .quote-pointer { position: absolute; left: 590px; top: 302px; }
  .author {
    position: absolute; left: 0; width: 1200px; top: 332px; text-align: center;
    font-family: "Poppins", sans-serif; font-weight: 700; font-size: 12px; color: var(--white);
  }
  .slider-dots { position: absolute; left: 588px; top: 370px; }

  .services { position: absolute; left: 0; top: 455px; width: 1200px; height: 91px; }
  .services .section-title { top: 40px; font-size: 22px; color: var(--ink); font-weight: 600; }
  .services-intro {
    position: absolute; left: 0; width: 1200px; top: 71px; text-align: center;
    font-size: 9.6px; color: var(--muted);
  }
</style>
</head>
<body>
<div class="page">
  <div class="top-band"></div>

  <section class="testimonials">
    <div class="testimonials-backdrop" role="img" aria-label="Black and white photo of people seated at a window counter overlooking a city skyline"></div>
    <h2 class="section-title">Testimonials</h2>
    <div class="avatar" role="img" aria-label="Round client photo of a coffee corner"></div>
    <div class="quote-card">
      <p>"Awesome theme with great design and helpfull support. If you don’t know how to code your own PressKit theme, but you still want a good-looking website for your business, Brightly might be exactly what you need. It is a slick theme with a lot of of features to choose from. You can customize whatever section you want and you can rest assure that no matter what device your website is viewed on – it looks great."</p>
    </div>
    <svg class="quote-pointer" width="20" height="11" viewBox="0 0 20 11"><polygon points="0,0 20,0 10,10" fill="#ffffff"/></svg>
    <div class="author">Clara Benton</div>
    <svg class="slider-dots" width="26" height="10" viewBox="0 0 26 10">
      <circle cx="5" cy="5" r="3" fill="rgba(255,255,255,0.35)"/>
      <circle cx="20" cy="5" r="3" fill="#ffffff"/>
    </svg>
  </section>

  <section class="services">
    <h2 class="section-title">Services</h2>
    <p class="services-intro">In order to help you grow your business, our carefully selected experts can advise you in in the following areas:</p>
  </section>
</div>
</body>
</html>
```